Fennick Medical - Flyer

We are a full service pharmacy that specializes in diabetic testing and medications. We research the patient's insurance to maximize their insurance benefit and then deliver the medications monthly directly to the patient's doorstep, for free! We save the patient, time and money every month.
We would love a flyer that we can distribute to Doctor's offices and patients that sum up our pharmacy. Emphasis on saving money, time, and getting the best quality supplies by maximizing their insurance. We want it to be eye catching, clean, and professional.
You can use our logo or feel free to make your own design.
diabetic patients wanting to save money
Insurance

```html
<!DOCTYPE html>
<html lang="en">
<head>
<meta charset="utf-8">
<title>Fennick Medical – Flyer</title>
<link rel="stylesheet" href="https://fonts.googleapis.com/css2?family=Oswald:wght@700&family=Open+Sans:wght@400;600&display=swap">
<style>
  :root {
    --orange: #f39a1e;
    --orange-light: #f8b24a;
    --orange-deep: #e9861a;
    --teal: #2aa3a4;
    --teal-light: #56c0bd;
    --white: #ffffff;
    --photo-grey: #8f8f8f;
    --photo-skin: #c9a08a;
  }
  * { margin: 0; padding: 0; box-sizing: border-box; }
  html, body { width: 1200px; height: 567px; overflow: hidden; background: var(--white); }
  .flyer {
    position: relative;
    width: 1200px;
    height: 567px;
    overflow: hidden;
    background: linear-gradient(135deg, var(--teal-light), var(--teal));
  }
  .flyer__shapes { position: absolute; inset: 0; }
  .benefits {
    position: absolute;
    left: 32px;
    top: 40px;
    list-style: none;
  }
  .benefits__item {
    display: flex;
    align-items: center;
    height: 105px;
    font-family: "Oswald", sans-serif;
    font-weight: 700;
    font-size: 70px;
    letter-spacing: -0.3px;
    word-spacing: -10px;
    color: var(--white);
    text-transform: uppercase;
  }
  .benefits__item::before {
    content: "";
    width: 17px;
    height: 17px;
    border-radius: 50%;
    background: var(--white);
    margin-right: 22px;
    flex: none;
  }
  .tagline {
    position: absolute;
    left: 71px;
    top: 364px;
    font-family: "Open Sans", sans-serif;
    font-size: 25px;
    letter-spacing: 0.8px;
    line-height: 34px;
    color: var(--white);
  }
  .website {
    position: absolute;
    left: 71px;
    top: 480px;
    font-family: "Open Sans", sans-serif;
    font-weight: 600;
    font-size: 22px;
    letter-spacing: 0.6px;
    color: var(--white);
  }
</style>
</head>
<body>
<main class="flyer">
  <svg class="flyer__shapes" width="1200" height="567" viewBox="0 0 1200 567">
    <defs>
      <radialGradient id="orangeGlow" cx="0.3" cy="0.45" r="0.75">
        <stop offset="0" stop-color="var(--orange-light)"/>
        <stop offset="1" stop-color="var(--orange-deep)"/>
      </radialGradient>
      <radialGradient id="meterPhoto" cx="0.55" cy="0.5" r="0.6">
        <stop offset="0" stop-color="var(--photo-skin)"/>
        <stop offset="0.55" stop-color="#a99489"/>
        <stop offset="1" stop-color="var(--photo-grey)"/>
      </radialGradient>
    </defs>
    <polygon class="banner" points="0,0 705,0 930,260 700,525 470,567 0,567" fill="url(#orangeGlow)"/>
    <circle class="badge__ring" cx="935" cy="288" r="302" fill="var(--orange)"/>
    <circle class="badge__frame" cx="935" cy="288" r="284" fill="var(--white)"/>
    <circle class="badge__photo" cx="935" cy="288" r="266" fill="url(#meterPhoto)"
            role="img" aria-label="Photo of hands testing blood sugar with a glucose meter and a finger prick"/>
  </svg>

  <ul class="benefits">
    <li class="benefits__item">Discounts</li>
    <li class="benefits__item">Personal Service</li>
    <li class="benefits__item">Home Delivery</li>
  </ul>

  <p class="tagline">A new way to manage your diabetes<br>monitoring and prescriptions -<br>direct to your door!</p>
  <p class="website">www.fennickmedical.com</p>
</main>
</body>
</html>
```